Exciting Personal Development Book Cover: FIND ZEN NOW!

Design a Book Cover for my personal development book.
Title: Find Zen Now!
Author: Marcus Telly
Tagline: A real-life solution to get unstuck and break free

My picture must make up the front cover as I need to build my brand and people should recognise me on book shelves. Bold and catchy. How you do it is up to you. There must be space for a short testimonial from a famous person who is currently reading my book. I uploaded a sample of what I made in Photoshop but I don't have design skills.

I've added a PDF of my book so you can read the chapter index and introduction to get a sense of the content.

Target Market(s)

Personal Development Self-Help Market

Industry/Entity Type

Personal Development

Font styles to use
Serif
Sans Serif

Requirements
Must have
• My picture as hero image on cover.
Nice to have
• Must have Title, Tagline and my author name. If possible ZEN stands for 'Zeal, Energy & Nerve' If there is a way to fit this somewhere great. If it's too much then it can go somewhere on the back.

```html
<!DOCTYPE html>
<html lang="en">
<head>
<meta charset="utf-8">
<title>Find Zen Now! — Book Cover</title>
<link href="https://fonts.googleapis.com/css2?family=Anton&family=Oswald:wght@600;700&family=Montserrat:wght@500&display=swap" rel="stylesheet">
<style>
  :root {
    --stage: #1ea6e0;
    --ink: #0b0d0f;
    --band: #111315;
    --sky-top: #7fb9c4;
    --sky-mid: #1f4f5c;
    --sky-low: #0a1216;
    --brand-blue: #1c9fe0;
    --pale-blue: #a9dcf5;
    --white: #ffffff;
  }
  * { margin: 0; padding: 0; box-sizing: border-box; }
  html, body { width: 1121px; height: 1200px; overflow: hidden; }
  body { background: var(--stage); position: relative; }

  .cover {
    position: absolute; left: 180px; top: 60px;
    width: 760px; height: 1080px; overflow: hidden;
    background: var(--sky-low);
  }
  .city-scene {
    position: absolute; inset: 0;
    background:
      radial-gradient(ellipse 60% 35% at 38% 8%, var(--sky-top) 0%, rgba(127,185,196,0) 70%),
      linear-gradient(180deg, var(--sky-mid) 0%, #173a44 35%, var(--sky-low) 75%, #050708 100%);
  }
  .author-photo {
    position: absolute; right: 0; top: 90px;
    width: 345px; height: 990px;
    background: linear-gradient(180deg, #6d6159 0%, #c9a58c 20%, #eeeeee 35%, #f4f4f4 70%, #dcdcdc 100%);
  }
  .tagline-band {
    position: absolute; left: 0; top: 28px; width: 100%; height: 62px;
    background: var(--band);
    display: flex; align-items: center; justify-content: center; gap: 10px;
    font-family: "Oswald", sans-serif; font-weight: 700; font-size: 30px;
    letter-spacing: 0.2px;
  }
  .tagline-lead { color: var(--brand-blue); }
  .tagline-key { color: var(--white); }

  .title { position: absolute; left: 78px; top: 120px; font-family: "Anton", sans-serif; line-height: 1; }
  .title-top { display: block; font-size: 200px; color: var(--ink); letter-spacing: -2px; }
  .title-acronym { position: relative; display: block; font-size: 170px; color: var(--brand-blue); margin-top: -6px; letter-spacing: -2px; }
  .acronym-meaning {
    position: absolute; left: 4px; top: 68px;
    font-family: "Montserrat", sans-serif; font-weight: 500; font-size: 21px;
    color: var(--white); letter-spacing: 1px; white-space: nowrap;
  }
  .title-bottom { display: block; font-size: 230px; color: var(--pale-blue); margin-top: -10px; letter-spacing: -3px; }

  .author { position: absolute; left: 118px; top: 830px; font-family: "Anton", sans-serif; font-size: 92px; line-height: 1.02; }
  .author-first { display: block; color: var(--brand-blue); }
  .author-last { display: block; color: var(--pale-blue); }
</style>
</head>
<body>
  <main class="cover">
    <div class="city-scene" role="img" aria-label="Dusky aerial view of a city with highways under a glowing sky"></div>
    <div class="author-photo" role="img" aria-label="Portrait of the author smiling in a white shirt with a tattooed forearm"></div>

    <div class="tagline-band">
      <span class="tagline-lead">A real-life solution to get</span>
      <span class="tagline-key">UNSTUCK AND BREAK FREE</span>
    </div>

    <h1 class="title">
      <span class="title-top">FIND</span>
      <span class="title-acronym">ZEN<span class="acronym-meaning">ZEAL, ENERGY &amp; NERVE</span></span>
      <span class="title-bottom">NOW!</span>
    </h1>

    <p class="author">
      <span class="author-first">MARCUS</span>
      <span class="author-last">TELLY</span>
    </p>
  </main>
</body>
</html>
```